Young judge needs a website to publish and to connect

I would like to have a website where I can publish my articles in public law. I am judge at the Alpine Civic Appeals Chamber. Therefore, the website must have a calm, friendly and fairly neutral design. Also, it should be mobile friendly and easy to use.

On my website, I want to

- publish articles such as https://www.quorvely.com/notes/how-win-court-tobias-wrenholt/ and get feedbacks from my colleagues
- generate interest for my project on 'Rules and Ballots - Notes from the Dais', a book that I would like to publish in 2020 and which brings together my publications on public law (http://www.statutewell.ch/content/english/profil/publikationen.html ).
- provide updates for my university courses on constitutional, administrative and international law.

For that purpose, I would kindly ask you to suggest a website that communicates a fresh approach to the work of a young judge in constitutional and administrative law. Please have in mind that I do not only sit on the bench, but that I also work in academia. Therefore, it should be suitable for an audience from both university and law practice. The website should replace the existing website on www.statutewell.ch that I designed when still working as a lawyer. Thank you.

Target Market(s)

Academica, law firms, courts

Industry/Entity Type

University

Contact Information for Business Card

Tobias Wrenholt
Judge
Alpine Civic Appeals Chamber
M +41 78 5XX 9X 2X

Logo Text

Notes from the Dais

Number of Pages Required

5+ page

Font styles to use
Sans Serif

Colors
0455a3

Requirements
Must have
• - a page where I can publish and get feedbacks
• - a page about my project on law and politics
• - a page where I can provide updates for my university courses on constitutional, administrative and international law
• - page where I can list current and planned projects
• - a collaborative, young and fresh approach
Nice to have
• - a page reserved for my colleagues at the Alpine Civic Appeals Chamber where I can alert them about to possibility to collaborate (if possibly password protected) and where they may suggest what to contribute to a specific project
Should not have
• anything which might to suggest that I want to make money with it, bragging or pretentious. Do not forget: I am judge, not a barrister.

```html
<!DOCTYPE html>
<html lang="en">
<head>
<meta charset="utf-8">
<title>How to win in court – Notes from the Dais</title>
<link rel="stylesheet" href="https://fonts.googleapis.com/css2?family=Montserrat:wght@500;600;700&family=Raleway:ital,wght@0,400;0,700;1,400&display=swap">
<style>
  :root {
    --brand-blue: #0455a3;
    --nav-accent: #f0b400;
    --ink: #3d3d3d;
    --ink-strong: #222;
    --paper: #ffffff;
    --footer-bg: #353535;
    --footer-ink: #d8d8d8;
    --footer-rule: #4a4a4a;
    --field-line: #d4d4d4;
  }
  * { box-sizing: border-box; margin: 0; padding: 0; }
  html, body {
    width: 1200px; height: 2848px; overflow: hidden;
    background: var(--paper);
    font-family: "Raleway", sans-serif;
    color: var(--ink);
    position: relative;
  }
  .site-header { position: absolute; top: 0; left: 0; width: 1200px; height: 129px; background: var(--brand-blue); color: var(--paper); }
  .wordmark {
    position: absolute; top: 26px; left: 0; right: 0;
    display: flex; justify-content: center; align-items: center; gap: 12px;
    font-family: "Montserrat", sans-serif; font-weight: 600; font-size: 26px; letter-spacing: 1px;
  }
  .wordmark-square { width: 14px; height: 14px; background: var(--paper); }
  .main-nav {
    position: absolute; top: 88px; left: 0; width: 1200px; height: 18px;
    font-family: "Montserrat", sans-serif; font-weight: 600; font-size: 13.5px;
  }
  .main-nav a, .main-nav span { position: absolute; top: 0; color: var(--paper); text-decoration: none; white-space: nowrap; }
  .main-nav .sep { color: var(--nav-accent); font-weight: 500; }
  .hero {
    position: absolute; top: 129px; left: 306px; width: 588px; height: 218px;
    background: linear-gradient(90deg, #6b4a35 0%, #8a6448 22%, #1f2d4d 40%, #263659 58%, #7d5a40 78%, #5c3f2c 100%);
  }
  .hero-title {
    position: absolute; top: 93px; left: 24px; white-space: nowrap;
    font-family: "Montserrat", sans-serif; font-weight: 700;
    font-size: 33px; letter-spacing: 6px; color: var(--paper);
  }
  .post-stats {
    position: absolute; top: 372px; left: 322px; width: 520px; height: 22px;
    font-family: "Montserrat", sans-serif; font-size: 13px; color: var(--brand-blue);
  }
  .post-stats .stat { position: absolute; top: 0; display: flex; align-items: center; gap: 14px; }
  .article-block {
    position: absolute; left: 306px; width: 588px;
    font-size: 10.6px; line-height: 14.3px; letter-spacing: 1px;
  }
  .article-block p { margin-bottom: 12px; }
  .article-block .step { font-style: italic; margin-bottom: 14px; }
  .article-block .tip { font-style: italic; margin-bottom: 14px; }
  .article-block h2 { font-size: 10.6px; font-weight: 700; color: var(--ink-strong); margin-bottom: 14px; }
  .figure-ballet { float: left; width: 326px; height: 139px; margin: 2px 18px 8px 0;
    background: radial-gradient(ellipse at 45% 45%, #5a5a62 0%, #1a1a1e 45%, #050505 100%); }
  .figure-award { float: right; width: 231px; height: 281px; margin: 2px 0 8px 18px;
    background: radial-gradient(ellipse at 50% 40%, #3a3f52 0%, #151821 60%, #0a0a0d 100%); }
  .figure-portrait { float: left; width: 182px; height: 171px; margin: 2px 16px 6px 0;
    background: linear-gradient(160deg, #d7e4e6 0%, #e03b74 35%, #b8c9b8 70%, #91a894 100%); }
  .comments-title {
    position: absolute; top: 2552px; left: 306px;
    font-family: "Montserrat", sans-serif; font-weight: 500; font-size: 19px;
    letter-spacing: 1.5px; color: var(--ink-strong);
  }
  .comment-field {
    position: absolute; top: 2588px; left: 306px; width: 588px; height: 58px;
    border: 1px solid var(--field-line); border-radius: 3px;
    font-size: 8.5px; color: #999; padding: 6px 8px;
  }
  .site-footer {
    position: absolute; top: 2672px; left: 0; width: 1200px; height: 176px;
    background: var(--footer-bg); color: var(--footer-ink);
    font-family: "Montserrat", sans-serif;
  }
  .footer-col { position: absolute; top: 22px; font-size: 11px; }
  .footer-col h3 { font-size: 12.5px; font-weight: 600; color: var(--paper); height: 22px; margin-bottom: 2px; }
  .footer-col ul { list-style: none; }
  .footer-col li { height: 23px; display: flex; align-items: center; gap: 12px; white-space: nowrap; }
  .footer-col .two-line { line-height: 11px; }
  .footer-col .dot { width: 7px; height: 7px; border-radius: 50%; background: var(--footer-ink); }
  .footer-rule { position: absolute; top: 148px; left: 430px; width: 340px; height: 1px; background: var(--footer-rule); }
  .copyright { position: absolute; top: 155px; left: 0; right: 0; text-align: center; font-size: 9px; color: #777; }
</style>
</head>
<body>
<header class="site-header">
  <div class="wordmark"><span class="wordmark-square"></span>Notes from the Dais</div>
  <nav class="main-nav">
    <svg style="position:absolute;left:322px;top:0" width="16" height="15" viewBox="0 0 18 17" aria-label="Home"><path d="M9 1 L17 8 H14 V16 H4 V8 H1 Z" fill="#fff"/></svg>
    <a style="left:385px">Articles</a>
    <span class="sep" style="left:484px">|</span>
    <a style="left:503px">Law and Politics</a>
    <span class="sep" style="left:631px">|</span>
    <a style="left:661px">University</a>
    <span class="sep" style="left:779px">|</span>
    <a style="left:824px">Projects</a>
  </nav>
</header>

<section class="hero" role="img" aria-label="Photograph of a lawyer in a navy suit and patterned tie against a wooden wall">
  <h1 class="hero-title">HOW TO WIN IN COURT</h1>
</section>

<div class="post-stats">
  <div class="stat" style="left:0"><svg width="17" height="19" viewBox="0 0 18 20"><path d="M9 1 L17 10 H12 V19 H6 V10 H1 Z" fill="#0455a3"/></svg>24</div>
  <div class="stat" style="left:143px"><svg width="17" height="17" viewBox="0 0 18 18"><path d="M7 2 L1 8 L7 14 V10 C12 10 15 12 17 16 C16 10 13 6 7 6 Z" fill="#0455a3"/></svg>13</div>
  <div class="stat" style="left:297px"><svg width="21" height="19" viewBox="0 0 22 20"><ellipse cx="11" cy="9" rx="10" ry="8" fill="#0455a3"/><path d="M4 14 L2 19 L9 16 Z" fill="#0455a3"/></svg>9</div>
  <div class="stat" style="left:491px"><svg width="19" height="19" viewBox="0 0 20 20"><circle cx="10" cy="10" r="10" fill="#0455a3"/><rect x="9" y="8.5" width="2" height="7" fill="#fff"/><circle cx="10" cy="5.5" r="1.3" fill="#fff"/></svg></div>
</div>

<div class="article-block" style="top:412px">
  <p>Whereas court proceedings tend to be complicated, judges are not. In fact, they are rather simple creatures. This is why they like it simple. And this is why it is not always that hard to win in court. All you have to do is reduce the complexity of the case.</p>
  <p style="margin-bottom:16px">To achieve this, just follow five simple steps:</p>
  <p class="step">1. Reduce it to the max.</p>
  <p class="step">2. Always remember that it is all about facts.</p>
  <p class="step">3. Make your brief look Italian.</p>
  <p class="step">4. Always keep a stiff upper lip.</p>
  <p class="step">5. Stop short of perfection, but do stop there.</p>
</div>

<div class="article-block" style="top:692px">
  <h2>1. Reduce it to the max</h2>
  <p>Now I do admit that making it sound simple is easier said than done. But it can be learned. And it is very rewarding. Ever observed that lawyer clearing the underbrush of that tedious and complex planning law case? It is about as beautiful as watching an Orchard III being converted into a Tablo mini. This is what judges love. They love plain. They love easy. And they love that counsel who explains them the case in three simple sentences.</p>
  <p style="margin-bottom:16px">Making it simple is challenging, but possible. When I was still practicing as a solicitor, I always asked my client to explain his case to his grandmother. After that, I tried to explain the case to my own grandmother. As she never had much time for detail, I tried to follow three simple steps:</p>
  <p class="tip">- Always start with your summary</p>
  <p class="tip">- Name three core arguments why the court should do what you want it to do.</p>
  <p class="tip">- Also, explain in two short sentences why it would be bad in the long run if the opposing party won the dispute.</p>
  <p>Ross Aldermoor's How to write like the nation's top advocates shows you how. It is a tremendous read. If you do not have it yet, buy it now. It will improve your writing enormously.</p>
</div>

<div class="article-block" style="top:1067px">
  <h2>2. It's all about facts</h2>
  <p style="margin-bottom:16px">I have not read Ross's book when I got my first trainee job in a law firm. In fact, I was a young law graduate with no experience whatsoever. In short, I thought that I was simply brilliant. So, after having been assigned a case of what I thought was a case of unfair dismissal, I started off with an elaborated statement about the law. I sent it to my boss, convinced that I would become partner of that firm soon. Luckily, I happened to have not only a very experienced, but also a very kind boss. So instead of transferring me to the firm's M&amp;A section immediately, he kindly pointed out to me that it would perhaps be helpful to first write a summary of the relevant facts. Also, it might help to do some more research on the government agency our client was working for at that time. Last but not least, my boss added, it always helps to talk to your client.</p>
  <div class="figure-ballet" role="img" aria-label="Photograph of a ballerina dancing on a dark stage"></div>
  <p style="margin-bottom:14px">I was shattered. And my dream of becoming a famous litigation partner seemed somehow futile. But I had learnt a rather important lesson. Litigation is all about facts. Counsel's main task is to present them in an accessible and convincing manner.</p>
  <p style="padding-left:0">I like to think of counsel as a ballet master. He is the choreographer of the case. What he cannot change is the ballet piece itself. So if your client comes up with the case of Swan Lake, don't try to transform it into the Sleeping Beauty. What you can do however, is impress the audience with an entirely new interpretation of Swan Lake. Counsel for the government might opt for a traditional interpretation. Your strategy might then consist of focussing on dynamic turns. That is still Swan Lake, but an entirely different and perhaps even more convincing interpretation.</p>
</div>

<div class="article-block" style="top:1506px">
  <h2>3. Make your brief look Italian</h2>
  <p style="margin-bottom:4px">This brings me to my third point. Whatever you write, it should be written Italian style. It should not only be neat, it should be short and simple.</p>
  <div class="figure-award" role="img" aria-label="Photograph of an actor in a dark suit holding up a film award trophy"></div>
  <p style="margin-bottom:16px">Remember Adrian Brolle receiving the Golden Reel for the Recital? Remember the suit he was wearing that night?</p>
  <p style="margin-bottom:16px">The suit was made by Ermanno Vellari. Vellari is the Paul Clemmer of fashion. His suits are timeless. You always look good in them, no matter what. It's like being represented by Professor Clemmer in the United States Supreme Court. Even if you lose the case, you are still looking good. So your briefs should look and feel like Vellari couture. Timeless. Simple. Elegant.</p>
  <p>By turning your writing into Vellari (or Paul Clemmer, for the matter), you show that you care. I cannot remember having dismissed a claim simply because the brief was written in Verdel with subtitles in Jolly Script. But then again, lack of style never helps really. It's a bit like turning up in court with a wet suit on a rainy day. Anyone would wonder why that counsel did not think of the umbrella or taking a taxi at least. So why not try Halden or Corvin next time?</p>
</div>

<div class="article-block" style="top:1905px">
  <h2>4. Always keep a stiff upper lip</h2>
  <p style="margin-bottom:16px">While the look and feel of your brief should be Italian, its content should be so British it even hurts. Understatement helps. Emotions never do. So always remember your stiffer upper lip.</p>
  <div class="figure-portrait" role="img" aria-label="Photograph of an elderly woman in a pink hat and pale coat"></div>
  <p>While still practicing at the bar, I would usually advise companies or small businesses in administrative law disputes. Now there is one thing which makes all the difference in that area. Your opposing party is not some unknown company or private individual, but the government. No matter whether it is a local authority or a government agency, your client is rather likely to be in contact with that government official again some day. Your client might need a planning permission for instance, or a renewal of his license, or simply an advice. This is why I tend to think that it is always a good idea to try and settle the case out of court. And even if no settlement is possible, I do think that it is of uttermost importance to be fair to your opposing party. So always leave a good impression. Be a good looser. And, if you win against the government (which does happen rather rarely), be a good winner. Your client will be thank you for that once he talks again to that government official about his license renewal.</p>
</div>

<div class="article-block" style="top:2243px">
  <h2>5. Stop short of perfection, but do stop there</h2>
  <p style="margin-bottom:16px">Finally, it's always a good idea to revise your brief the next day. Nothing is more disturbing than a claim with spelling mistakes, misleading citations, not to mention that case which helps the opposing party but not your client really.</p>
  <p style="margin-bottom:16px">Then again, any attempt to write that perfect brief will fail. So anything quite solid, convincing and elegant will do. The best revising time is spent in shortening the brief. So never stop short of perfection. But do stop there. Good luck!</p>
  <p style="margin-bottom:16px">Would you like to share your own experiences with good briefs? Anything that struck you as outstanding, convincing, even thrilling? Please do feel free to comment.</p>
  <p>Tobias Wrenholt is a judge and a writer. He would like to thank Dr Lena Holtvik for her helpful comments on the first draft of this post.</p>
</div>

<h2 class="comments-title">Comments</h2>
<div class="comment-field">Add a comment</div>

<footer class="site-footer">
  <div class="footer-col" style="left:426px">
    <h3 style="padding-left:16px">Get in touch</h3>
    <ul>
      <li><span class="dot"></span>Friendwall</li>
      <li><span class="dot"></span>Chirpline</li>
      <li><span class="dot"></span>Circleplus</li>
    </ul>
  </div>
  <div class="footer-col" style="left:576px">
    <h3>Explore</h3>
    <ul>
      <li>Articles</li>
      <li>Law and Politics</li>
      <li>University</li>
      <li>Planned Projects</li>
    </ul>
  </div>
  <div class="footer-col" style="left:718px">
    <h3>Profile</h3>
    <ul>
      <li>Tobias Wrenholt</li>
      <li class="two-line">Selected German<br>Publications</li>
      <li>Clients</li>
      <li>Contact</li>
    </ul>
  </div>
  <div class="footer-rule"></div>
  <div class="copyright">© 2017</div>
</footer>
</body>
</html>
```